Calloway Dental Care

I need a nice business card design that is double sided. This is for a dental surgery. I have already had a logo designed and just need the business card put together.

It needs to be in a format such that I can make new business cards if new dentists begin working for me. Hence I need to be able to change the text in order to have new names written on new cards.

The front will have the following text:

Dr Tariq Mansour
B. Med. Sci. QBTU B.Dent. Brel. Uni

The logo will appear somewhere on the front. This is attached.

In addition will be the following writing that also needs to appear on the front of the card, perhaps at the bottom on the left side will be:

Shop 4, 212-240 Parlow Street, North Sydney, NSW, 2060

and at the bottom on the right side will be:
(02) 5550 1736
e: info@callowaydentalcare.com.au
www.callowaydentalcare.com.au

On the back of the card will be a section for a map to be drawn (I have uploaded a picture) and also a section written as follows:

"Your next appointment is: (a line needs to be here to write date and time)"

Also I need two lines for two appointments to be written.

Thanks for your efforts!

```html
<!DOCTYPE html>
<html lang="en">
<head>
<meta charset="utf-8">
<title>Calloway Dental Care – Business Card</title>
<link rel="stylesheet" href="https://fonts.googleapis.com/css2?family=Noto+Serif:wght@400&display=swap">
<style>
  :root {
    --ink: #231f20;
    --card-edge: #6b6b6b;
    --rule-blue: #7e9cc4;
    --brand-blue: #2f6aa8;
    --brand-cyan: #14c4f0;
    --map-grey: #dcdcdc;
    --paper: #ffffff;
  }
  * { margin: 0; padding: 0; box-sizing: border-box; }
  html, body {
    width: 1004px;
    height: 1200px;
    overflow: hidden;
    background: var(--paper);
  }
  body {
    position: relative;
    font-family: "Noto Serif", Georgia, serif;
    color: var(--ink);
  }
  .card-art {
    position: absolute;
    inset: 0;
    width: 1004px;
    height: 1200px;
  }
  .text { position: absolute; white-space: nowrap; line-height: 1; }

  /* Front */
  .brand-mark {
    position: absolute;
    left: 155px;
    top: 88px;
    width: 90px;
    height: 90px;
    border-radius: 50%;
    background: var(--brand-cyan);
  }
  .brand-name {
    left: 60px;
    top: 206px;
    width: 280px;
    text-align: center;
    font-size: 27px;
    color: var(--brand-blue);
  }
  .dentist-name { left: 433px; top: 146px; font-size: 50px; font-weight: 400; }
  .credentials { left: 472px; top: 212px; font-size: 25px; }
  .contact { left: 472px; top: 318px; font-size: 26px; line-height: 43px; }
  .contact p { margin: 0; }
  .address {
    right: 586px;
    top: 448px;
    text-align: right;
    font-size: 26px;
    line-height: 40px;
    font-style: normal;
  }
  .corner-accent {
    position: absolute;
    left: 872px;
    top: 444px;
    width: 72px;
    height: 72px;
    background: linear-gradient(135deg, var(--brand-blue), var(--brand-cyan));
    opacity: 0.85;
  }

  /* Back */
  .map-area {
    position: absolute;
    left: 34px;
    top: 654px;
    width: 332px;
    height: 507px;
    border-radius: 16px;
    background: linear-gradient(160deg, #e2e2e2, var(--map-grey));
  }
  .appointment-title { left: 413px; top: 758px; font-size: 40px; }
</style>
</head>
<body>

<svg class="card-art" viewBox="0 0 1004 1200" aria-hidden="true">
  <defs>
    <linearGradient id="divider-fade" x1="0" y1="0" x2="0" y2="1">
      <stop offset="0" stop-color="#ffffff"/>
      <stop offset="0.5" stop-color="#222222"/>
      <stop offset="1" stop-color="#ffffff"/>
    </linearGradient>
  </defs>

  <path class="card-front-edge" d="M1.5 193 A192 192 0 0 1 193 1.5 H1002 V572 H1.5 Z"
        fill="var(--paper)" stroke="var(--card-edge)" stroke-width="1.5"/>

  <path class="name-rule" d="M412 143 V190 Q412 200 422 200 H945 Q955 200 955 210 V236"
        fill="none" stroke="var(--rule-blue)" stroke-width="1.5"/>

  <rect class="divider" x="441" y="408" width="3" height="116" fill="url(#divider-fade)"/>

  <path class="card-back-edge" d="M1.5 625 H730 A272 150 0 0 1 1002 775 V1196 H1.5 Z"
        fill="var(--paper)" stroke="var(--card-edge)" stroke-width="1.5"/>

  <g class="appointment-lines" fill="none" stroke="var(--rule-blue)" stroke-width="1.5">
    <path d="M413 844 V868 Q413 878 423 878 H944"/>
    <path d="M413 934 V960 Q413 970 423 970 H944"/>
    <path d="M413 1024 V1050 Q413 1060 423 1060 H944"/>
  </g>
</svg>

<section class="card-front">
  <div class="brand-mark"></div>
  <div class="text brand-name">Calloway Dental Care</div>

  <h1 class="text dentist-name">Dr. Tariq Mansour</h1>
  <div class="text credentials">B. Med. Sci. QBTU B.Dent. Brel. Uni</div>

  <div class="text contact">
    <p>(02) 5550 1736</p>
    <p>e: info@callowaydentalcare.com.au</p>
    <p>www.callowaydentalcare.com.au</p>
  </div>

  <address class="text address">
    Shop 4, 212-240 Parlow Street<br>
    North Sydney, NSW, 2060
  </address>

  <div class="corner-accent" role="img" aria-label="Decorative blue tile accent"></div>
</section>

<section class="card-back">
  <div class="map-area" role="img" aria-label="Street map showing the location of Calloway Dental Care near the surrounding streets and highway"></div>
  <div class="text appointment-title">Your next appointment is:</div>
</section>

</body>
</html>
```